HVAC Design Services

I want a brochure to market my services. I own TOVEN Design Services LLC. I specialize in Mechanical Design with HVAC Design being my
specialty. I also do Plumbing and Civil Design. I have a strong resume with over 30 years experience. I was the Lead Mechanical Designer and Cad Manager for the mechanical group at an Architectural Engineering company for over 10 years.

I would like a professional looking brochure to pass out to engineering offices. I am targeting over-load work, when an office is so busy they need temporary help. Special project. Freeing up the engineer with my experience and capability to work with little to no direction .

1. HVAC Design
a) Calculate cfm
b) Layout and route ductwork
c) Size Ductwork
d) Choose and Layout grilles, registers and diffusers
e) Choose equipment and locate on plans
f) Create HVAC Floor Plans, Sections, Details and Schedules

2. Plumbing Design
a) Layout and route plumbing
b) Size piping
c) Create Plumbing Floor Plans, Sections, Details and Schedules.

3. AutoCAD 3D Modeling

4. Civil and GIS experience

5. AutoCAD 3D Modeling

6. Some Electrical and Structural Design experience

```html
<!DOCTYPE html>
<html lang="en">
<head>
<meta charset="utf-8">
<title>TOVEN Design Services LLC – Brochure</title>
<link href="https://fonts.googleapis.com/css2?family=Montserrat:wght@400;500;600;700&family=Oswald:wght@500&display=swap" rel="stylesheet">
<style>
  :root {
    --green: #7cb541;
    --navy: #0f1f3a;
    --slate: #626262;
    --frame: #bcbdbf;
    --paper: #f6f7f9;
    --white: #ffffff;
    --ink-gray: #555555;
  }
  html, body {
    margin: 0;
    padding: 0;
    width: 1200px;
    height: 1199px;
    overflow: hidden;
    background: var(--white);
  }
  .canvas {
    position: relative;
    width: 1200px;
    height: 1199px;
  }
  .flyer {
    position: absolute;
    width: 517px;
    height: 659px;
    background: var(--frame);
  }
  .flyer svg {
    position: absolute;
    left: 13px;
    top: 13px;
    width: 490px;
    height: 634px;
  }
  .flyer--cover { left: 61px; top: 100px; }
  .flyer--services { left: 622px; top: 440px; }
  .sans { font-family: "Montserrat", sans-serif; }
  .condensed { font-family: "Oswald", sans-serif; font-weight: 500; }
</style>
</head>
<body>
<div class="canvas">

  <!-- Cover flyer -->
  <section class="flyer flyer--cover">
    <svg viewBox="0 0 613 792" xmlns="http://www.w3.org/2000/svg">
      <defs>
        <linearGradient id="atriumTone" x1="0" y1="0" x2="1" y2="1">
          <stop offset="0" stop-color="#cfd2cc"/>
          <stop offset="0.45" stop-color="#6b7468"/>
          <stop offset="0.7" stop-color="#2b312c"/>
          <stop offset="1" stop-color="#9aa095"/>
        </linearGradient>
      </defs>
      <rect class="photo" role="img" aria-label="Photo looking down a tall building atrium lined with hanging plants" x="0" y="0" width="613" height="792" fill="url(#atriumTone)"/>

      <rect x="18" y="57" width="344" height="44" fill="var(--navy)"/>
      <text class="sans" x="25" y="93" fill="var(--white)" font-size="37" font-weight="700">OVER-LOADED?</text>
      <rect x="18" y="107" width="275" height="46" fill="var(--green)"/>
      <text class="sans" x="25" y="143" fill="var(--white)" font-size="37" font-weight="700">GET A HAND</text>

      <polygon points="0,392 430,635 0,755" fill="var(--green)"/>
      <polygon points="430,635 613,585 613,711" fill="var(--slate)"/>
      <polygon points="0,755 430,635 613,711 613,792 0,792" fill="var(--paper)"/>

      <text class="sans" x="17" y="590" fill="var(--white)" font-size="19" font-weight="700">MARCUS DELGADO</text>
      <text class="sans" x="16" y="625" fill="var(--white)" font-size="30" font-weight="700">(555)-014-2870</text>
      <text class="sans" x="20" y="648" fill="var(--white)" font-size="11" font-weight="500" letter-spacing="1">Sr. MECHANICAL/CIVIL</text>
      <text class="sans" x="20" y="664" fill="var(--white)" font-size="11" font-weight="500" letter-spacing="1">PROJECT DESIGNER</text>

      <g class="brand-name">
        <text class="sans" x="424" y="757" fill="#2b2b2b" font-size="26" font-weight="600" text-anchor="middle" textLength="190" lengthAdjust="spacingAndGlyphs">TOVEN DESIGN</text>
        <text class="sans" x="424" y="774" fill="#2b2b2b" font-size="12" font-weight="600" text-anchor="middle" letter-spacing="2.5">SERVICES LLC</text>
      </g>
    </svg>
  </section>

  <!-- Services flyer -->
  <section class="flyer flyer--services">
    <svg viewBox="0 0 613 792" xmlns="http://www.w3.org/2000/svg">
      <defs>
        <linearGradient id="draftTone" x1="0" y1="0" x2="1" y2="1">
          <stop offset="0" stop-color="#3a2c22"/>
          <stop offset="0.4" stop-color="#d9d3c8"/>
          <stop offset="0.75" stop-color="#efece6"/>
          <stop offset="1" stop-color="#2a2420"/>
        </linearGradient>
        <linearGradient id="stripTone" x1="0" y1="0" x2="0" y2="1">
          <stop offset="0" stop-color="#3b3f4a"/>
          <stop offset="0.35" stop-color="#8a5443"/>
          <stop offset="0.65" stop-color="#2f3033"/>
          <stop offset="1" stop-color="#8c8c8c"/>
        </linearGradient>
      </defs>
      <rect x="0" y="0" width="613" height="792" fill="var(--green)"/>
      <polygon class="photo" role="img" aria-label="Photo of a designer's hands sketching a building plan on paper with a scale ruler" points="0,0 613,0 613,174 466,239 0,145" fill="url(#draftTone)"/>
      <polygon points="466,239 613,174 613,312" fill="var(--slate)"/>
      <polygon class="photo" role="img" aria-label="Photo strip: laptop with 3D model, pipe fittings, HVAC condenser units and a stairwell" points="283,224 413,258 413,624 283,598" fill="url(#stripTone)"/>
      <polygon points="0,524 613,687 613,792 0,792" fill="var(--paper)"/>
      <polygon points="368,604 564,647 564,792 368,792" fill="var(--slate)"/>

      <text class="condensed" x="19" y="239" fill="var(--white)" font-size="36">HVAC DESIGN</text>
      <g class="checks" fill="none" stroke="var(--white)" stroke-width="2.2" stroke-linecap="round" stroke-linejoin="round">
        <polyline points="20,268 25,274 35,262"/>
        <polyline points="20,296 25,302 35,290"/>
        <polyline points="20,323 25,329 35,317"/>
        <polyline points="20,350 25,356 35,344"/>
        <polyline points="20,395 25,401 35,389"/>
        <polyline points="20,441 25,447 35,435"/>
      </g>
      <g class="sans" fill="var(--white)" font-size="15.5" font-weight="500">
        <text x="47" y="275">Calculate cfm</text>
        <text x="47" y="303">Layout and route ductwork</text>
        <text x="47" y="329">Size Ductwork</text>
        <text x="47" y="356">Choose and Layout grilles,</text>
        <text x="47" y="374">registers and diffusers</text>
        <text x="47" y="401">Choose equipment and</text>
        <text x="47" y="420">locate on plans</text>
        <text x="47" y="447">Create HVAC Floor Plans,</text>
        <text x="47" y="465">Sections, Details and</text>
        <text x="47" y="483">Schedules</text>
      </g>

      <g class="condensed" fill="var(--white)" font-size="22">
        <text x="432" y="344">AUTOCAD 3D</text>
        <text x="432" y="372">MODELING</text>
        <text x="432" y="427">CIVIL AND GIS</text>
        <text x="432" y="454">EXPERIENCE</text>
        <text x="432" y="510" textLength="143" lengthAdjust="spacingAndGlyphs">SOME ELECTRICAL</text>
        <text x="432" y="537" textLength="138" lengthAdjust="spacingAndGlyphs">AND STRUCTURAL</text>
        <text x="432" y="564" textLength="161" lengthAdjust="spacingAndGlyphs">DESIGN EXPERIENCE</text>
      </g>

      <text class="condensed" x="19" y="637" fill="var(--ink-gray)" font-size="36">PLUMBING DESIGN</text>
      <g class="checks" fill="none" stroke="var(--ink-gray)" stroke-width="2.2" stroke-linecap="round" stroke-linejoin="round">
        <polyline points="21,659 26,665 36,653"/>
        <polyline points="21,708 26,714 36,702"/>
        <polyline points="21,737 26,743 36,731"/>
      </g>
      <g class="sans" fill="var(--green)" font-size="15.5" font-weight="500">
        <text x="48" y="666">Layout and route</text>
        <text x="48" y="685">plumbing</text>
        <text x="48" y="715">Size piping</text>
        <text x="48" y="744">Create Plumbing Floor Plans,</text>
        <text x="48" y="762">Sections, Details and Schedules.</text>
      </g>

      <g class="brand-name">
        <text class="sans" x="466" y="722" fill="var(--white)" font-size="22" font-weight="600" text-anchor="middle" textLength="162" lengthAdjust="spacingAndGlyphs">TOVEN DESIGN</text>
        <text class="sans" x="466" y="738" fill="var(--white)" font-size="10.5" font-weight="600" text-anchor="middle" letter-spacing="2.2">SERVICES LLC</text>
      </g>
    </svg>
  </section>

</div>
</body>
</html>
```